Mining services business card

I need a business card for a mining services company, we provide consultancy work, Engineers, and personnel. We also provide contract mining in both development and production capabilities. We also provide ground support systems for both the surface/underground mining and also the civil construction industries. We are currently providing services in Australia and China.

Target Market(s)

The Mining and Civil industries, both in Australia and abroad.

Industry/Entity Type

Construction

Logo Text

KORVEX Mining & Civil

Logo styles of interest
Pictorial/Combination Logo
Abstract Logo
Lettermark Logo
Requirements
Must have
• The Business name needs to fit the following format
KORVEX
Mining & Civil
The KORVEX must be the same width as the Mining & Civil
Nice to have
• I would like to feel cutting edge, modern and new. Some reference to Mining and Civil works would be good.

```html
<!DOCTYPE html>
<html lang="en">
<head>
<meta charset="utf-8">
<title>KORVEX Mining &amp; Civil – Business Card</title>
<link rel="stylesheet" href="https://fonts.googleapis.com/css2?family=Roboto+Condensed:wght@300;400;700&display=swap">
<style>
  :root {
    --backdrop: #0a0a0a;
    --card-white: #eceef0;
    --card-grey: #d9dcde;
    --brand-red: #c1000f;
    --brand-red-dark: #a8000d;
    --ink: #1c1c1e;
    --bar: #1c1c1e;
    --on-red: #ffffff;
  }
  * { box-sizing: border-box; margin: 0; padding: 0; }
  html, body {
    width: 900px; height: 1200px; overflow: hidden;
    background: var(--backdrop);
    font-family: "Roboto Condensed", "Arial Narrow", sans-serif;
  }
  .canvas { position: relative; width: 900px; height: 1200px; }
  .card {
    position: absolute; left: 103px; width: 682px; height: 395px;
    background: var(--card-white); overflow: hidden;
  }
  .card--front { top: 110px; }
  .card--back { top: 661px; }
  .card__shapes { position: absolute; inset: 0; width: 100%; height: 100%; }

  .wordmark { position: absolute; overflow: visible; }
  .wordmark text {
    fill: var(--ink);
    font-family: "Roboto Condensed", "Arial Narrow", sans-serif;
    font-weight: 700;
  }
  .card--front .wordmark { left: 54px; top: 140px; width: 240px; height: 110px; }
  .card--back .wordmark { left: 163px; top: 118px; width: 355px; height: 160px; }

  .contact {
    position: absolute; right: 33px; top: 148px;
    text-align: right; color: var(--on-red);
    font-size: 18px; font-weight: 300; line-height: 22.5px;
  }
  .contact__name { font-weight: 700; font-size: 20px; line-height: 24px; }
  .contact__role { font-weight: 400; font-size: 20px; line-height: 26px; margin-bottom: 10px; }
  .contact__label { font-weight: 700; }
  .contact__email { margin-top: 2px; }

  .web-bar {
    position: absolute; left: 305px; right: 33px; top: 342px; height: 24px;
    background: var(--bar); color: var(--on-red);
    font-size: 18px; font-weight: 400; letter-spacing: 1.6px;
    line-height: 24px; text-align: right; padding-right: 4px;
  }
</style>
</head>
<body>
<main class="canvas">

  <section class="card card--front" aria-label="Business card front">
    <svg class="card__shapes" viewBox="0 0 682 395" aria-hidden="true">
      <polygon points="332,0 467,0 397,145" fill="var(--card-grey)"/>
      <polygon points="467,0 682,0 682,395 289,395" fill="var(--brand-red)"/>
      <polygon points="289,395 360,240 430,395" fill="var(--brand-red-dark)"/>
    </svg>

    <svg class="wordmark" viewBox="0 0 240 110" role="img" aria-label="KORVEX Mining &amp; Civil">
      <text x="0" y="62" font-size="70" textLength="240" lengthAdjust="spacingAndGlyphs">KORVEX</text>
      <text x="0" y="100" font-size="28" textLength="240" lengthAdjust="spacing">MINING &amp; CIVIL</text>
    </svg>

    <div class="contact">
      <p class="contact__name">DANIEL REEVE</p>
      <p class="contact__role">CONTRACTOR</p>
      <p>58 Quarry Ridge Road</p>
      <p>Kalgan, WA 6330</p>
      <p><span class="contact__label">P</span> 08 9417 2256</p>
      <p><span class="contact__label">F</span> 08 9417 2257</p>
      <p class="contact__email">daniel.reeve@korvex.com.au</p>
    </div>

    <div class="web-bar">WWW.KORVEXCIVIL.COM.AU</div>
  </section>

  <section class="card card--back" aria-label="Business card back">
    <svg class="card__shapes" viewBox="0 0 682 395" aria-hidden="true">
      <polygon points="587,0 682,0 682,395 545,395 655,120" fill="var(--brand-red)"/>
      <polygon points="655,120 682,55 682,300" fill="var(--brand-red-dark)"/>
      <polygon points="610,240 682,300 682,395 640,395" fill="var(--brand-red-dark)" opacity="0.7"/>
    </svg>

    <svg class="wordmark" viewBox="0 0 355 160" role="img" aria-label="KORVEX Mining &amp; Civil">
      <text x="0" y="89" font-size="108" textLength="355" lengthAdjust="spacingAndGlyphs">KORVEX</text>
      <text x="0" y="141" font-size="41" textLength="355" lengthAdjust="spacing">MINING &amp; CIVIL</text>
    </svg>
  </section>

</main>
</body>
</html>
```